Business card for auto dealership

Looking for a clean modern design.
Would like attached logo incorporated

Industry/Entity Type

Car dealership

Contact Information for Business Card

Name, website, phone, cell, fax, email

```html
<!DOCTYPE html>
<html lang="en">
<head>
<meta charset="utf-8">
<title>Halden Truck &amp; Auto Sales — Business Card</title>
<link rel="stylesheet" href="https://fonts.googleapis.com/css2?family=Lobster&family=Open+Sans:wght@400;700&display=swap">
<style>
  :root {
    --backdrop: #0c0d0d;
    --card: #222424;
    --card-edge: #b98d62;
    --cream: #f0e3c4;
    --copper: #c4885a;
    --rule: #d9c79f;
  }
  * { margin: 0; padding: 0; box-sizing: border-box; }
  html, body { width: 1200px; height: 975px; overflow: hidden; background: var(--backdrop); }
  .canvas { position: relative; width: 1200px; height: 975px; }

  .card {
    position: absolute;
    width: 560px; height: 320px;
    background: var(--card);
    border: 1.5px solid var(--card-edge);
    border-radius: 2px;
    font-family: "Open Sans", sans-serif;
    color: var(--cream);
  }
  .card--front { left: 580px; top: 110px; display: flex; align-items: center; justify-content: center; }
  .card--back { left: 60px; top: 545px; }

  .brand { color: var(--copper); font-family: "Open Sans", sans-serif; font-weight: 700; text-align: center; line-height: 1; }
  .brand__name { display: block; }
  .brand__tagline { display: block; letter-spacing: 0.06em; }
  .card--front .brand__name { font-size: 84px; }
  .card--front .brand__tagline { font-size: 19px; margin-top: 10px; }

  .holder { position: absolute; left: 34px; top: 30px; }
  .holder__name { font-family: "Lobster", cursive; font-size: 32px; color: var(--cream); line-height: 1.1; }
  .holder__email { font-size: 13px; color: var(--cream); margin-top: 2px; }

  .divider { position: absolute; left: 28px; top: 100px; width: 400px; height: 1.5px; background: var(--rule); }

  .contacts { position: absolute; left: 34px; top: 116px; list-style: none; }
  .contacts li { display: flex; align-items: center; gap: 10px; font-size: 15px; line-height: 26px; }
  .contacts svg { width: 13px; height: 13px; fill: var(--cream); }

  .card--back .brand { position: absolute; right: 40px; top: 118px; }
  .card--back .brand__name { font-size: 46px; }
  .card--back .brand__tagline { font-size: 11px; margin-top: 6px; }

  .website { position: absolute; right: 34px; bottom: 28px; font-size: 16px; font-weight: 700; color: var(--cream); }
</style>
</head>
<body>
<main class="canvas">

  <section class="card card--front" aria-label="Card front">
    <div class="brand">
      <span class="brand__name">Halden</span>
      <span class="brand__tagline">TRUCK &amp; AUTO SALES</span>
    </div>
  </section>

  <section class="card card--back" aria-label="Card back">
    <div class="holder">
      <h1 class="holder__name">Dana Whitlow</h1>
      <p class="holder__email">dana@haldenauto.com</p>
    </div>
    <div class="divider"></div>
    <ul class="contacts">
      <li>
        <svg viewBox="0 0 16 16" aria-hidden="true"><path d="M3.5 1l2.5 3-1.5 2c1 2 3 4 5 5l2-1.5 3 2.5-1.5 2.5C7 15 1 9 1 2.5z"/></svg>
        555-014-2368
      </li>
      <li>
        <svg viewBox="0 0 16 16" aria-hidden="true"><path d="M4 1h8v14H4zM5.5 2.5v10h5v-10z"/></svg>
        555-019-4427
      </li>
      <li>
        <svg viewBox="0 0 16 16" aria-hidden="true"><path d="M4 1h8v4H4zM1 6h14v6h-3v3H4v-3H1zM5.5 10v3.5h5V10z"/></svg>
        555-012-8853
      </li>
    </ul>
    <div class="brand">
      <span class="brand__name">Halden</span>
      <span class="brand__tagline">TRUCK &amp; AUTO SALES</span>
    </div>
    <p class="website">Haldenauto.com</p>
  </section>

</main>
</body>
</html>
```